Energieberater sucht Flyer-Design
Zielgruppe
Ich bin Energieberater, habe mich vor kurzem selbstständig gemacht und möchte nun meine Bekanntheit steigern. Meine Zielgruppe sind Immobilieneigentümer sowie Immobiliensuchende, welchen ich eine fundierte Energieberatung mit Sanierungskonzepten sowie die Erstellung von Energieausweisen bieten kann.
Aufgabenstellung
Ich benötige einen Flyer, welchen ich regional verteilen möchte. Der Flyer soll quadratisch (148 x 148) erstellt werden.
Der Flyer sollte mein Logo, meine Kontaktdaten, die unten aufgeführten Dienstleistungen sowie einen Gutschein enthalten und insbesondere der Bekanntheits-/Imagesteigerung dienen.
Vorhandene Punkte sollen sein:
- Erstellung von Energieausweisen für Vermietung und Verkauf
- Energieberatung
- Sanierungs- und Modernisierungskonzepte
- Fördermittelberatung
Der Flyer soll die Möglichkeit bieten, am Rand abgeschnitten zu werden. Dort soll ein Gutschein aufgeführt werden mit 25 € Rabatt für einen Energieausweis.
Meine Kontaktdaten können Sie der angehängten Visitenkarte entnehmen.

```html
<!DOCTYPE html>
<html lang="de">
<head>
<meta charset="utf-8">
<title>Flyer Energieberatung Berwald</title>
<link rel="stylesheet" href="https://fonts.googleapis.com/css2?family=Fira+Sans+Condensed:wght@400;500;600&family=Montserrat:wght@600;700&display=swap">
<style>
  :root {
    --petrol: #2a7a97;
    --petrol-dark: #226780;
    --slate: #505254;
    --stage: #c7c7c7;
    --white: #ffffff;
    --grey-text: #6b6b6b;
    --lime: #a5b21e;
    --yellow: #e3c40b;
    --orange: #e57f12;
    --red: #d7131b;
    --tag-grey: #5c5d60;
  }
  * { box-sizing: border-box; margin: 0; padding: 0; }
  html, body { width: 1200px; height: 623px; overflow: hidden; }
  body {
    background: var(--stage);
    position: relative;
    font-family: "Fira Sans Condensed", sans-serif;
  }
  .flyer {
    position: absolute;
    top: 39px;
    width: 538px;
    height: 538px;
    background: var(--white);
    overflow: hidden;
    box-shadow: 0 4px 10px rgba(0,0,0,.25);
  }
  .flyer--front { left: 40px; }
  .flyer--back { left: 618px; }

  /* Front */
  .brand {
    position: absolute;
    left: 52px; top: 0;
    height: 159px;
    display: flex;
    align-items: center;
    gap: 14px;
  }
  .brand__mark {
    width: 16px; height: 16px;
    background: var(--petrol);
  }
  .brand__name {
    font-weight: 500;
    font-size: 30px;
    color: var(--petrol);
    letter-spacing: .5px;
  }
  .front-band {
    position: absolute; left: 0; top: 159px;
    width: 100%; height: 14px;
    background: var(--petrol);
  }
  .front-photo {
    position: absolute; left: 160px; top: 173px;
    width: 378px; height: 365px;
    background:
      linear-gradient(90deg, #fff 0%, rgba(255,255,255,0) 45%),
      linear-gradient(180deg, rgba(255,255,255,0) 70%, #fff 100%),
      radial-gradient(ellipse at 62% 55%, #f1d2c0 0%, #e8c0aa 35%, #f3e4db 70%, #fbf5f1 100%);
  }
  .services {
    position: absolute; left: 31px; top: 0;
    list-style: none;
  }
  .service {
    position: absolute;
    left: 0;
    width: 300px;
    padding-left: 18px;
    font-weight: 500;
    font-size: 20.5px;
    line-height: 21.5px;
    color: var(--petrol);
    white-space: nowrap;
  }
  .service::before {
    content: "";
    position: absolute; left: 0; top: 7px;
    width: 9px; height: 9px;
    background: var(--bullet);
  }
  .service--ausweis { top: 245px; --bullet: var(--lime); }
  .service--beratung { top: 341px; --bullet: var(--yellow); }
  .service--konzepte { top: 392px; --bullet: var(--orange); }
  .service--foerder { top: 467px; --bullet: var(--red); }

  /* Back */
  .intro {
    position: absolute; left: 0; top: 0;
    width: 315px; height: 249px;
    background: var(--petrol);
    color: var(--white);
    padding: 28px 20px 0 29px;
    font-size: 12.7px;
    line-height: 14.1px;
  }
  .intro p + p { margin-top: 28px; }
  .contact {
    position: absolute; left: 319px; top: 0;
    width: 219px; height: 249px;
    background: var(--slate);
    color: var(--white);
    padding: 0 0 0 28px;
  }
  .contact__mark {
    position: absolute; left: 28px; top: 40px;
    width: 18px; height: 18px;
    background: var(--orange);
  }
  .contact__name {
    position: absolute; left: 28px; top: 102px;
    font-weight: 600;
    font-size: 17.5px;
    line-height: 17.5px;
  }
  .contact__list {
    position: absolute; left: 28px; top: 155px;
    list-style: none;
    font-size: 10px;
    line-height: 14px;
  }
  .contact__item {
    display: flex; gap: 4px; align-items: flex-start;
  }
  .contact__item svg { flex: none; margin-top: 2px; }
  .contact__item--phone { margin-top: 14px; }
  .back-photo {
    position: absolute; left: 0; top: 249px;
    width: 538px; height: 247px;
    background:
      linear-gradient(90deg, #fff 0%, rgba(255,255,255,0) 40%),
      radial-gradient(ellipse at 70% 45%, #d8c39a 0%, #e4dccd 35%, #eeeeee 65%, #f3f3f3 100%);
  }
  .voucher {
    position: absolute; left: 27px; top: 330px;
    width: 186px; height: 118px;
    transform: rotate(-9deg);
    transform-origin: left top;
    clip-path: polygon(0 6%, 85% 0, 100% 24%, 100% 100%, 0 100%);
    background: linear-gradient(180deg, var(--tag-grey) 0 58%, var(--petrol) 58% 100%);
    border-radius: 6px;
    color: var(--white);
    font-family: "Montserrat", sans-serif;
    box-shadow: 0 3px 6px rgba(0,0,0,.2);
  }
  .voucher__amount {
    position: absolute; left: 52px; top: 8px;
    font-weight: 700; font-size: 32px; line-height: 32px;
  }
  .voucher__label {
    position: absolute; left: 52px; top: 40px;
    font-weight: 700; font-size: 22px; line-height: 22px;
  }
  .voucher__hole {
    position: absolute; right: 14px; top: 40px;
    width: 9px; height: 9px; border-radius: 50%;
    background: #eee;
  }
  .voucher__for {
    position: absolute; left: 0; right: 0; top: 74px;
    text-align: center;
    font-weight: 600; font-size: 14px; line-height: 15px;
  }
  .web-band {
    position: absolute; left: 0; bottom: 0;
    width: 100%; height: 42px;
    background: var(--petrol);
    color: var(--white);
    font-family: "Montserrat", sans-serif;
    font-weight: 600;
    font-size: 19px;
    display: flex; align-items: center; justify-content: center;
    letter-spacing: .2px;
  }
</style>
</head>
<body>

<section class="flyer flyer--front">
  <div class="brand">
    <span class="brand__mark"></span>
    <span class="brand__name">Energieberatung Berwald</span>
  </div>
  <div class="front-band"></div>
  <div class="front-photo" role="img" aria-label="Foto: zwei Hände umschließen ein kleines weißes Papierhaus mit farbiger Energieeffizienzskala von A bis G"></div>
  <ul class="services">
    <li class="service service--ausweis">Erstellung von<br>Energieausweisen<br>für Vermietung und Verkauf</li>
    <li class="service service--beratung">Energieberatung</li>
    <li class="service service--konzepte">Sanierungs- und<br>Modernisierungskonzepte</li>
    <li class="service service--foerder">Fördermittelberatung</li>
  </ul>
</section>

<section class="flyer flyer--back">
  <div class="intro">
    <p>Wir unterstützen Sie bei der Erstellung eines Energieausweises, nehmen eine Begutachtung der Gebäudesubstanz vor, zeigen den energetischen IST-Zustand anhand der Energieeffizienzklassen auf und leiten Modernisierungs-empfehlungen zur Verbesserung der Energieeffizienz ab.</p>
    <p>Als Käufer erhalten Sie mit Übergabe des Energieausweises einen Wegweiser, um die Kosten der anstehenden Modernisierung einschätzen zu können und einen Überblick über den baulichen Zustand der Immobilie zu erhalten.</p>
  </div>
  <div class="contact">
    <span class="contact__mark"></span>
    <h2 class="contact__name">Energieberatung<br>Jonas Berwald</h2>
    <ul class="contact__list">
      <li class="contact__item">
        <svg width="7" height="9" viewBox="0 0 7 9"><path d="M3.5 0A3.3 3.3 0 0 0 .2 3.3C.2 5.8 3.5 9 3.5 9s3.3-3.2 3.3-5.7A3.3 3.3 0 0 0 3.5 0zm0 4.6a1.3 1.3 0 1 1 0-2.6 1.3 1.3 0 0 1 0 2.6z" fill="#fff"/></svg>
        <span>Am Lindenhang 14<br>35683 Dillstadt</span>
      </li>
      <li class="contact__item contact__item--phone">
        <svg width="8" height="8" viewBox="0 0 8 8"><path d="M1.6.3 2.8 2 2.1 3a4.6 4.6 0 0 0 2.9 2.9l1-.7 1.7 1.2-.6 1.3C3.4 7.8.2 4.6.3.9z" fill="#fff"/></svg>
        <span>+49 0151 55501234</span>
      </li>
      <li class="contact__item">
        <svg width="8" height="8" viewBox="0 0 8 8"><rect x="0" y="1.5" width="8" height="5.5" fill="#fff"/><path d="M0 1.5 4 4.5 8 1.5" stroke="#505254" stroke-width=".8" fill="none"/></svg>
        <span>info@energieberatung-berwald.de</span>
      </li>
    </ul>
  </div>
  <div class="back-photo" role="img" aria-label="Illustration: aufgeschnittenes Einfamilienhaus mit sichtbarer Dämmung auf Bauplänen und Energieeffizienzskala"></div>
  <div class="voucher">
    <span class="voucher__amount">25 €</span>
    <span class="voucher__label">RABATT</span>
    <span class="voucher__hole"></span>
    <span class="voucher__for">für einen<br>Energieausweis</span>
  </div>
  <div class="web-band">www.energieberatung-berwald.de</div>
</section>

</body>
</html>
```